Business Cards

Business card design for my company.
I would like the card's background colour to be black. You can also see our web site to get an idea of our brand. https://www.dlqmarrowfield.com.au/
- Name
- Email

```html
<!DOCTYPE html>
<html lang="en">
<head>
<meta charset="utf-8">
<title>DLQ Marrowfield – Business Card</title>
<link href="https://fonts.googleapis.com/css2?family=Questrial&display=swap" rel="stylesheet">
<style>
  :root {
    --page: #1d1e1f;
    --card: #3a3b3d;
    --green: #1b9a4b;
    --white: #ffffff;
    --muted: #e4e4e4;
  }
  * { margin: 0; padding: 0; box-sizing: border-box; }
  html, body {
    width: 1200px; height: 1043px; overflow: hidden;
    background: var(--page);
    font-family: "Questrial", "Century Gothic", sans-serif;
  }
  .card {
    position: absolute; left: 205px;
    width: 790px; height: 436px;
    background: var(--card);
    overflow: hidden;
  }
  .card--front { top: 96px; }
  .card--back { top: 580px; }

  .front-panel { position: absolute; inset: 0; }

  .brand-vertical {
    position: absolute;
    right: 18px; top: 50%;
    transform: translateY(-50%);
    writing-mode: vertical-rl;
    color: var(--white);
    font-size: 30px; font-weight: 400;
    letter-spacing: 3px;
    white-space: nowrap;
    line-height: 1;
  }

  .person { position: absolute; left: 39px; top: 48px; }
  .person__name { font-size: 31px; font-weight: 400; color: var(--white); line-height: 1; }
  .person__first { color: var(--green); }
  .person__role { font-size: 15px; color: var(--muted); margin-top: 6px; }
  .person__rule { width: 152px; height: 3px; background: var(--green); margin-top: 12px; }

  .accent-bar {
    position: absolute; left: 2px; top: 346px;
    width: 4px; height: 58px; border-radius: 2px;
    background: var(--green);
  }
  .contacts { position: absolute; left: 40px; top: 340px; list-style: none; }
  .contacts li {
    display: flex; align-items: center; gap: 10px;
    font-size: 16px; color: var(--muted); height: 21px;
  }
  .contacts svg { width: 13px; height: 13px; fill: var(--green); flex: none; }

  .brand-mark {
    position: absolute; left: 0; right: 0; top: 186px;
    display: flex; justify-content: center; align-items: center; gap: 16px;
    color: var(--white); font-size: 42px; letter-spacing: 5px;
  }
  .brand-mark__square { width: 22px; height: 22px; background: var(--green); }

  .web-line {
    position: absolute; left: 39px; right: 39px; top: 384px;
    display: flex; align-items: center; gap: 14px;
    color: var(--white); font-size: 17px;
  }
  .web-line__rule { flex: 1; height: 2px; background: var(--muted); }
  .web-line__domain { color: var(--green); }
</style>
</head>
<body>
  <section class="card card--front">
    <svg class="front-panel" viewBox="0 0 790 436" aria-hidden="true">
      <polygon points="441,0 790,0 790,436 525,436 337,157" fill="var(--green)"/>
    </svg>
    <div class="brand-vertical">DLQ MARROWFIELD</div>

    <div class="person">
      <h1 class="person__name"><span class="person__first">Glen</span> Tarrant</h1>
      <p class="person__role">General Manager</p>
      <div class="person__rule"></div>
    </div>

    <div class="accent-bar"></div>
    <ul class="contacts">
      <li>
        <svg viewBox="0 0 24 24"><path d="M6.6 10.8a15.1 15.1 0 0 0 6.6 6.6l2.2-2.2c.3-.3.7-.4 1-.2 1.1.4 2.3.6 3.6.6.6 0 1 .4 1 1V20c0 .6-.4 1-1 1C10.6 21 3 13.4 3 4c0-.6.4-1 1-1h3.5c.6 0 1 .4 1 1 0 1.3.2 2.5.6 3.6.1.3 0 .7-.2 1z"/></svg>
        0412 555 830
      </li>
      <li>
        <svg viewBox="0 0 24 24"><path d="M2 5h20v14H2z M2 5l10 7 10-7" /></svg>
        info@dlqmarrowfield.com.au
      </li>
      <li>
        <svg viewBox="0 0 24 24"><path d="M12 2a7 7 0 0 0-7 7c0 5.2 7 13 7 13s7-7.8 7-13a7 7 0 0 0-7-7zm0 9.5A2.5 2.5 0 1 1 12 6.5a2.5 2.5 0 0 1 0 5z"/></svg>
        Brackenvale, Northshire, Australia
      </li>
    </ul>
  </section>

  <section class="card card--back">
    <div class="brand-mark">
      <span class="brand-mark__square"></span>
      <span class="brand-mark__name">DLQ MARROWFIELD</span>
    </div>
    <div class="web-line">
      <span class="web-line__rule"></span>
      <span class="web-line__url">www.<span class="web-line__domain">dlqmarrowfield</span>.com</span>
      <span class="web-line__rule"></span>
    </div>
  </section>
</body>
</html>
```